Eco friendly Swedish beauty products sold in aluminum bottles - label design needed

We need help in designing a series of stick on labels for 80 ml (2.7 fl. oz.) aluminum bottles containing beauty products such as soaps, shampoo etc. The diameter of the bottle is 36 mm and the body of the bottles measures approx. 106 mm.
It is important for us that the label has a simplistic and clean feel with few colors (and the right ones!) and that the label helps amplify this product being both better and a more sustainable alternative to many of our plastic bottle competitors. The design and label should communicate the feel of an Eco-friendly, sustainable and modern brand of high quality - and with a Swedish concept.
We are using Montserrat font in our materials. Find attached information of preferred colors, the bottles and one example of our logotype. I am also available on e-mail should further information be needed.

Looking forward and very excited to receive your suggestions.
Note that we are expecting to start selling a series of approximately 10 different products where I will need one "master design" and then only smaller changes for each of the different products.

Target Market(s)

People whom are aware and not only look at price tag. Private and commercial market.

Industry/Entity Type

Beauty

Font styles to use
Other font styles liked:
• Montserrat

Requirements
Must have
• It must give the feel of being both better and a more sustainable alternative to many of our plastic bottle competitors.
Nice to have
• Simplistic. Clean. Clear.
Should not have
• Wrong colors, too complex designs.

```html
<!DOCTYPE html>
<html lang="en">
<head>
<meta charset="utf-8">
<title>Label series – conditioner and shampoo</title>
<link rel="stylesheet" href="https://fonts.googleapis.com/css2?family=Jost:wght@300;400;600&display=swap">
<style>
  :root {
    --canvas: #ffffff;
    --cream: #f5efe6;
    --tan: #ddb398;
    --ink-on-cream: #dcb294;
    --ink-on-tan: #f7f1e8;
  }
  * { margin: 0; padding: 0; box-sizing: border-box; }
  html, body {
    width: 1200px;
    height: 1200px;
    overflow: hidden;
    background: var(--canvas);
    font-family: "Jost", "Montserrat", sans-serif;
  }
  .sheet {
    position: relative;
    width: 1200px;
    height: 1200px;
  }
  .label {
    position: absolute;
    top: 52px;
    width: 371px;
    height: 1095px;
  }
  .label--conditioner {
    left: 202px;
    background: var(--cream);
    color: var(--ink-on-cream);
  }
  .label--shampoo {
    left: 600px;
    background: var(--tan);
    color: var(--ink-on-tan);
  }
  .brand-name {
    position: absolute;
    top: 96px;
    left: 71px;
    font-size: 34px;
    font-weight: 400;
    letter-spacing: 1px;
    line-height: 1;
    white-space: nowrap;
  }
  .product-name {
    position: absolute;
    left: 71px;
    top: 795px;
    font-size: 44px;
    font-weight: 600;
    letter-spacing: 2.2px;
    line-height: 1;
    white-space: nowrap;
  }
  .product-purpose {
    position: absolute;
    left: 71px;
    top: 867px;
    font-size: 24.5px;
    font-weight: 300;
    line-height: 1;
    white-space: nowrap;
  }
  .product-volume {
    position: absolute;
    left: 71px;
    top: 1030px;
    font-size: 19.5px;
    font-weight: 300;
    line-height: 1;
    white-space: nowrap;
  }
</style>
</head>
<body>
  <main class="sheet">
    <section class="label label--conditioner">
      <p class="brand-name">Lindhav</p>
      <h2 class="product-name">conditioner</h2>
      <p class="product-purpose">for dry &amp; damaged hair</p>
      <p class="product-volume">80ml (2.7 fl. oz.)</p>
    </section>
    <section class="label label--shampoo">
      <p class="brand-name">Lindhav</p>
      <h2 class="product-name">shampoo</h2>
      <p class="product-purpose">for dry &amp; damaged hair</p>
      <p class="product-volume">80ml (2.7 fl. oz.)</p>
    </section>
  </main>
</body>
</html>
```